I need a DVD cover for a training package contained on a disc. There are four modules within the resource so I need these to be visible on the cover. They are:
Cultural Competence Healthcare Provision
Provision of Care to CALD Women having Babies in Australia
Cultural Considerations in Aged Care Provision
Cultural Competence in Mental Health

I have attached a cd cover with an image of a waratah. This is Bellmore Ridge Valley Health's logo so needs to appear on the front cover also.
The smaller logo with the waratah also needs to be on the front cover. Please note these are the only copies I could obtain so if the quality is too poor you may need to reproduce.

The following should appear on the back cover:
‘Pathways to Inclusive Patient Support’ is a collaborative achievement of the Multicultural Health Liaison Officers in Acute Care, Obstetrics, Aged Care and Mental Health under the guidance of the Director, Multicultural Health Service in Bellmore Ridge Valley Local Health District. Staff members from the specialist teams and community members graciously contributed to the production of podcasts and video clips.
Photography, video clips and technical support was provided by Daniel Follett - E-learning Developer and Designer - Lumen Tutors.
This project was coordinated by Colleen Bastow, Multicultural Health Liaison Officer (Acute Care, Lower Brindlewood Coastal Hospital Network).

```html
<!DOCTYPE html>
<html lang="en">
<head>
<meta charset="utf-8">
<title>Pathways to Inclusive Patient Support – DVD Cover and Disc</title>
<link rel="stylesheet" href="https://fonts.googleapis.com/css2?family=Tinos:wght@400;700&family=Arimo:wght@400;700&display=swap">
<style>
  :root {
    --stage: #e8eaee;
    --blue-deep: #0b4a96;
    --blue-mid: #1b68bb;
    --blue-band: #2a7bcc;
    --wave: #3d86d0;
    --white: #ffffff;
    --ink-soft: #e3eefa;
    --brand-red: #d0202e;
    --brand-navy: #1d3f7a;
    --disc-face: #fbfbfc;
    --disc-ring: #d9dbe0;
    --disc-hub: #c6c9cf;
    --photo-a: #c9b7a2;
    --photo-b: #9fb4c9;
  }
  * { box-sizing: border-box; margin: 0; padding: 0; }
  html, body { width: 1200px; height: 799px; overflow: hidden; }
  body {
    background: var(--stage);
    font-family: "Arimo", Arial, sans-serif;
    position: relative;
  }

  /* ---------- Disc (sits behind the cover) ---------- */
  .disc {
    position: absolute;
    left: 560px; top: 240px;
    width: 460px; height: 460px;
    z-index: 1;
  }
  .disc-logo {
    position: absolute;
    left: 300px; top: 310px;
    width: 150px;
    display: flex; align-items: flex-start; gap: 6px;
    color: var(--brand-navy);
    font-size: 9.5px; font-weight: 700; line-height: 1.3;
  }
  .disc-logo .logo-square {
    flex: none; width: 12px; height: 12px; margin-top: 1px;
    background: var(--brand-navy);
  }

  /* ---------- Front cover ---------- */
  .cover {
    position: absolute;
    left: 300px; top: 90px;
    width: 370px; height: 620px;
    background: linear-gradient(180deg, var(--blue-mid) 0%, var(--blue-deep) 55%, var(--blue-mid) 100%);
    overflow: hidden;
    z-index: 2;
    box-shadow: 6px 8px 18px rgba(0,0,0,0.18);
  }
  .photo-band {
    position: absolute;
    left: 0; top: 24px; width: 100%; height: 88px;
    background: var(--blue-band);
    display: flex; gap: 5px;
    padding: 8px 12px;
  }
  .photo {
    flex: 1;
    background: linear-gradient(160deg, var(--photo-a), var(--photo-b));
    border: 2px solid var(--white);
  }
  .title {
    position: absolute;
    left: 22px; top: 206px; width: 330px;
    font-family: "Tinos", "Times New Roman", serif;
    font-weight: 700;
    color: var(--white);
    font-size: 26px;
    line-height: 1.4;
  }
  .modules {
    position: absolute;
    left: 22px; top: 300px; width: 336px;
    list-style: none;
    color: var(--ink-soft);
    font-size: 10.5px;
    line-height: 1.55;
    font-weight: 700;
  }
  .cover-base {
    position: absolute;
    left: 0; bottom: 0; width: 100%; height: 240px;
  }
  .brand-circle {
    position: absolute;
    left: -70px; bottom: -60px;
    width: 210px; height: 210px;
    border-radius: 50%;
    background: var(--brand-red);
  }
  .cover-logo {
    position: absolute;
    left: 150px; bottom: 22px;
    color: var(--white);
    font-size: 11px; font-weight: 700;
  }
</style>
</head>
<body>

<section class="disc" aria-label="Disc label">
  <svg viewBox="0 0 460 460" width="460" height="460" aria-hidden="true">
    <circle cx="230" cy="230" r="227" fill="var(--disc-face)" stroke="var(--disc-ring)" stroke-width="3"/>
    <circle cx="230" cy="230" r="66" fill="#eceef1" stroke="var(--disc-ring)" stroke-width="2"/>
    <circle cx="230" cy="230" r="42" fill="var(--disc-hub)"/>
    <circle cx="230" cy="230" r="25" fill="var(--stage)" stroke="#b4b8bf" stroke-width="2"/>
  </svg>
  <div class="disc-logo">
    <span class="logo-square"></span>
    <span>Bellmore Ridge Valley Health<br>Bellmore Ridge Valley Local Health District</span>
  </div>
</section>

<section class="cover" aria-label="DVD front cover">
  <div class="photo-band">
    <div class="photo" role="img" aria-label="Photograph of a family with a young child"></div>
    <div class="photo" role="img" aria-label="Photograph of a carer with an older patient"></div>
    <div class="photo" role="img" aria-label="Photograph of older relatives together"></div>
    <div class="photo" role="img" aria-label="Photograph of a smiling older man"></div>
  </div>

  <h1 class="title">Pathways to Inclusive<br>Patient Support</h1>

  <ul class="modules">
    <li>Cultural Competence Healthcare Provision</li>
    <li>Provision of Care to CALD Women having Babies in Australia</li>
    <li>Cultural Considerations in Aged Care Provision</li>
    <li>Cultural Competence in Mental Health</li>
  </ul>

  <svg class="cover-base" viewBox="0 0 370 240" aria-hidden="true">
    <path d="M0 100 C100 70 250 130 370 90 L370 240 L0 240 Z" fill="var(--wave)" opacity="0.45"/>
    <polyline points="0,150 130,150 145,150 155,118 166,182 177,135 186,150 370,150"
              fill="none" stroke="#ffffff" stroke-width="1.5" opacity="0.75"/>
    <path d="M282 104 v20 M272 114 h20" stroke="#ffffff" stroke-width="3" opacity="0.8"/>
  </svg>

  <div class="brand-circle" aria-hidden="true"></div>
  <div class="cover-logo">Bellmore Ridge Valley Health</div>
</section>

</body>
</html>
```